business card design for luxurious real estate brand

using the attached logo, i am looking for a 2-sided business card design. the back should be the gold logo on black background. the front needs to include: gold logo, name, phone, email, and website

Industry/Entity Type

real estate

Contact Information for Business Card

logo, name, email, phone, website

Font styles to use
Sans Serif

```html
<!DOCTYPE html>
<html lang="en">
<head>
<meta charset="utf-8">
<title>Casa Vantaro – Business Card</title>
<link rel="stylesheet" href="https://fonts.googleapis.com/css2?family=Poppins:wght@400;500;600&display=swap">
<style>
  :root {
    --stage: #1c1c1d;
    --card: #161617;
    --gold: #fdd00f;
    --white: #ffffff;
  }
  * { margin: 0; padding: 0; box-sizing: border-box; }
  html, body {
    width: 1200px; height: 1200px; overflow: hidden;
    background: var(--stage);
    font-family: "Poppins", sans-serif;
  }
  .stage {
    width: 1200px; height: 1200px;
    display: flex; flex-direction: column; align-items: center; justify-content: center;
    gap: 60px;
  }
  .card {
    position: relative;
    width: 900px; height: 514px;
    background: var(--card);
    overflow: hidden;
    box-shadow: 0 14px 40px rgba(0,0,0,0.55);
  }
  /* back side */
  .card-back { display: flex; align-items: center; justify-content: center; }
  .brand {
    display: flex; align-items: center; gap: 22px;
    color: var(--gold);
    font-weight: 500; font-size: 46px; letter-spacing: 0.3em;
  }
  .brand-square { width: 30px; height: 30px; background: var(--gold); }
  /* front side */
  .accent-bar {
    position: absolute; left: 70px; top: 72px;
    width: 18px; height: 46px; background: var(--gold);
  }
  .identity { position: absolute; left: 120px; top: 64px; }
  .person-name {
    color: var(--white); font-weight: 600; font-size: 30px; letter-spacing: 0.06em;
  }
  .person-role {
    color: var(--gold); font-weight: 400; font-size: 20px; letter-spacing: 0.04em; margin-top: 2px;
  }
  .contact-list {
    position: absolute; left: 70px; bottom: 60px;
    list-style: none; display: flex; flex-direction: column; gap: 10px;
  }
  .contact-item {
    display: flex; align-items: center; gap: 16px;
    color: var(--white); font-size: 22px; letter-spacing: 0.03em;
  }
  .contact-icon { width: 22px; height: 22px; flex: none; }
  .gold-panel {
    position: absolute; right: 0; top: 150px;
    width: 300px; height: 364px; background: var(--gold);
  }
</style>
</head>
<body>
<main class="stage">
  <section class="card card-back" aria-label="Card back">
    <div class="brand"><span class="brand-square"></span>CASA VANTARO</div>
  </section>

  <section class="card card-front" aria-label="Card front">
    <span class="accent-bar"></span>
    <div class="identity">
      <h1 class="person-name">MARCUS DELANEY</h1>
      <p class="person-role">CEO/FOUNDER</p>
    </div>
    <ul class="contact-list">
      <li class="contact-item">
        <svg class="contact-icon" viewBox="0 0 24 24" aria-hidden="true"><path fill="#fdd00f" d="M6.6 10.8a15.1 15.1 0 0 0 6.6 6.6l2.2-2.2a1 1 0 0 1 1-.25 11.4 11.4 0 0 0 3.6.57 1 1 0 0 1 1 1V20a1 1 0 0 1-1 1A17 17 0 0 1 3 4a1 1 0 0 1 1-1h3.5a1 1 0 0 1 1 1c0 1.25.2 2.45.57 3.57a1 1 0 0 1-.25 1z"/></svg>
        214-555-0182
      </li>
      <li class="contact-item">
        <svg class="contact-icon" viewBox="0 0 24 24" aria-hidden="true"><path fill="#fdd00f" d="M2 5h20v14H2z"/><path fill="none" stroke="#161617" stroke-width="1.6" d="M2 5l10 8 10-8"/></svg>
        marcus@casavantaro.com
      </li>
      <li class="contact-item">
        <svg class="contact-icon" viewBox="0 0 24 24" aria-hidden="true"><g fill="none" stroke="#fdd00f" stroke-width="2"><circle cx="12" cy="12" r="9.5"/><ellipse cx="12" cy="12" rx="4" ry="9.5"/><path d="M2.5 12h19M4 7h16M4 17h16"/></g></svg>
        www.casavantaro.com
      </li>
    </ul>
    <div class="gold-panel"></div>
  </section>
</main>
</body>
</html>
```